Business Card for Quillmark Ledger - A cannabis publication for executives.

I'd like some business cards for Quillmark Ledger. The logo is done (great job!) and I need a card design I will use with PRINTLY. I made it a short project to allow time for printing before an event. These will be standard sized cards (final artwork size 3.66" x 2.16" at 300dpi) with a final card size of 3.5" x 2.0". (See PRINTLY.com if you need more info.) I might try rounded corners but am not sure yet. I think the design will work okay with rounded.

Quillmark Ledger will be a bi-weekly publication for the cannabis industry. It is targeted to investors and industry executives, not consumers or pot smokers. So our market is more B2B. However I am open to creativity and making the card something people remark on.

My contact for card:

Dana Merrow
Founder/CEO
dana@quillmarkledger.example

2740 Harlow Avenue
Boston MA 02135
(617)555-0194

Target Market(s)

Executives, Industry people and investors in the Cannabis sector.

Contact Information for Business Card

PRINTLY does do double sided and the second side can be the same or different images. Only one side is required but use of the second side would be a bonus.

Font styles to use
Serif
Sans Serif
Decorative

Colors

Designer to choose colors to be used in the design.

Requirements
Must have
• Logo, contact info
Nice to have
• Style and design to make the card stand out in a crowd.

```html
<!DOCTYPE html>
<html lang="en">
<head>
<meta charset="utf-8">
<title>Quillmark Ledger — Business Card</title>
<link rel="stylesheet" href="https://fonts.googleapis.com/css2?family=Open+Sans:ital,wght@0,400;0,600;0,700;1,400&display=swap">
<style>
  :root {
    --brand-blue: #1175bf;
    --brand-green: #7aab37;
    --paper: #ffffff;
    --pattern-tint: #eef3ea;
    --pattern-tint-2: #e6eff6;
    --backdrop: #6e4c34;
    --ink-grey: #4a4a4a;
    --on-blue: #ffffff;
  }
  * { box-sizing: border-box; margin: 0; padding: 0; }
  html, body {
    width: 1200px; height: 987px; overflow: hidden;
    background: var(--backdrop);
    font-family: "Open Sans", Arial, sans-serif;
  }
  .card {
    position: absolute; left: 292px; width: 616px; height: 352px;
    background: var(--paper); overflow: hidden;
    box-shadow: 0 3px 8px rgba(0,0,0,.35);
  }
  .card--front { top: 130px; }
  .card--back { top: 505px; }

  .front-bands { position: absolute; inset: 0; width: 100%; height: 100%; }

  .wordmark {
    position: absolute; left: 0; right: 0;
    display: flex; align-items: center; justify-content: center; gap: 12px;
    color: var(--brand-blue); font-weight: 600; letter-spacing: -0.5px;
    white-space: nowrap;
  }
  .wordmark__dot { border-radius: 50%; background: var(--brand-green); flex: none; }
  .card--front .wordmark { top: 62px; font-size: 38px; }
  .card--front .wordmark__dot { width: 30px; height: 30px; }

  .holder { position: absolute; left: 0; right: 0; top: 174px; text-align: center; }
  .holder__name { color: var(--brand-blue); font-weight: 600; font-size: 20px; letter-spacing: .2px; }
  .holder__role { color: var(--brand-green); font-size: 15px; margin-top: 2px; }

  .contact-list { position: absolute; left: 34px; top: 258px; list-style: none; }
  .contact-list li {
    display: flex; align-items: center; gap: 8px;
    color: var(--on-blue); font-size: 15px; line-height: 24px;
  }
  .contact-list svg { width: 13px; height: 13px; fill: var(--on-blue); flex: none; }

  .address {
    position: absolute; right: 29px; top: 282px; text-align: right;
    color: var(--on-blue); font-size: 15px; line-height: 24px; font-style: normal;
  }

  .back-pattern {
    position: absolute; inset: 0;
    background: linear-gradient(135deg, var(--pattern-tint), var(--pattern-tint-2));
  }
  .card--back .wordmark { top: 140px; font-size: 52px; }
  .card--back .wordmark__dot { width: 40px; height: 40px; }
  .back-url {
    position: absolute; left: 0; right: 0; top: 286px; text-align: center;
    color: var(--ink-grey); font-style: italic; font-size: 15px; letter-spacing: 2.5px;
  }
</style>
</head>
<body>

<section class="card card--front" aria-label="Card front">
  <svg class="front-bands" viewBox="0 0 616 352" preserveAspectRatio="none" aria-hidden="true">
    <polygon points="0,141 308,296 616,141 616,352 0,352" fill="#1175bf"/>
    <polygon points="0,137 308,292 616,137 616,141 308,296 0,141" fill="#ffffff"/>
    <polygon points="0,126 308,281 616,126 616,137 308,292 0,137" fill="#7aab37"/>
  </svg>

  <div class="wordmark"><span class="wordmark__dot"></span><span>Quillmark Ledger</span></div>

  <div class="holder">
    <p class="holder__name">DANA MERROW</p>
    <p class="holder__role">Founder/CEO</p>
  </div>

  <ul class="contact-list">
    <li>
      <svg viewBox="0 0 24 24"><path d="M6.6 10.8a15.1 15.1 0 0 0 6.6 6.6l2.2-2.2c.3-.3.7-.4 1-.2 1.1.4 2.3.6 3.6.6.6 0 1 .4 1 1V20c0 .6-.4 1-1 1A17 17 0 0 1 3 4c0-.6.4-1 1-1h3.5c.6 0 1 .4 1 1 0 1.3.2 2.5.6 3.6.1.3 0 .7-.2 1z"/></svg>
      (617)555-0194
    </li>
    <li>
      <svg viewBox="0 0 24 24"><path d="M2 5h20v14H2z M3.5 6.5 12 13l8.5-6.5" fill="none" stroke="#fff" stroke-width="2"/></svg>
      dana@quillmarkledger.example
    </li>
    <li>
      <svg viewBox="0 0 24 24"><circle cx="12" cy="12" r="10" fill="none" stroke="#fff" stroke-width="2"/><path d="M2 12h20M12 2c3 3 3 17 0 20M12 2c-3 3-3 17 0 20" fill="none" stroke="#fff" stroke-width="1.6"/></svg>
      www.quillmarkledger.example
    </li>
  </ul>

  <address class="address">2740 Harlow Avenue<br>Boston MA 02135</address>
</section>

<section class="card card--back" aria-label="Card back">
  <div class="back-pattern" role="img" aria-label="Faint repeating pattern of the brand symbol in pale green and blue"></div>
  <div class="wordmark"><span class="wordmark__dot"></span><span>Quillmark Ledger</span></div>
  <p class="back-url">www.quillmarkledger.example</p>
</section>

</body>
</html>
```